Harbor Valley Pride Sponsorship

Harbor Valley Pride is looking for an updated sponsorship package design – included in the shared information is our sponsorship packaged used in 2017, 2018, and 2019.

The mission of Harbor Valley Pride is to create opportunities for integrating and promoting visibility for the lesbian. gay, bisexual and transgender community; promoting equal rights and diversity through public education and the arts; provide safe opportunities and venues for people to come out with the ability to express and celebrate their sexual identities.

Some images (because of their size) are not allowed to be uploaded... use the following link to access the full library of images, reference documents, and the full outline: https://files.examplecloud.net/share/7kQmZ2tVx9LpR4nWc8Hs3dYb

Sponsorship packet design details:
Final file type: .pdf and/or .ai/.eps
Orientation: Preferably landscape but not opposed to a portrait design.
Page count: estimated 6 with current content (not opposed to 8 pages)
Size: 8.5”x11”
Full bleed

Images:
Images for this design are shared in a folder “images for use in sponsorship packet” – please feel free to choose them as you see fit and we can make any notes after the first draft.

Creative Reference:
Additionally, provided are a few sponsorship packages that we like and feel that you might be able to take inspiration from – these are in a folder named “sponsorship packets we like”
Updates

I've updated all of the details of this project and would like to have completed asap. Thank you.

Target Market(s)

Primarily our target market is local and regional businesses that are interested in supporting JoyFair through sponsorship or might be interested in advertising opportunities.

Industry/Entity Type

LGBT

Font styles to use
Serif
Sans Serif

Colors

Designer to choose colors to be used in the design.

Requirements
Must have
• All sponsorship details

```html
<!DOCTYPE html>
<html lang="en">
<head>
<meta charset="utf-8">
<title>Harbor Valley Pride – JoyFair Sponsorship Packages</title>
<link rel="stylesheet" href="https://fonts.googleapis.com/css2?family=Oswald:wght@500&family=Montserrat:wght@400;600;700;800&family=Arimo:wght@400;700&display=swap">
<style>
:root{
  --bg:#e4e4e4;
  --orange:#e1482b;
  --purple:#4a3b93;
  --purple-dark:#3a2e7c;
  --green:#86bf45;
  --teal:#5fc4a7;
  --amber:#ee8b2c;
  --ink:#3a3a3a;
  --muted:#6b6b6b;
  --white:#ffffff;
  --sky:linear-gradient(180deg,#c9dbe8 0%,#b7c9d3 35%,#8e9b8a 62%,#6f8f5c 100%);
}
*{box-sizing:border-box;margin:0;padding:0}
html,body{width:1200px;height:3130px;overflow:hidden}
body{background:var(--bg);position:relative;font-family:"Arimo",Arial,sans-serif;color:var(--ink)}
.abs{position:absolute}
.page{position:absolute;background:var(--white);overflow:hidden;box-shadow:0 2px 10px rgba(0,0,0,.18)}
.photo{position:absolute;background:var(--sky)}
.brand{display:flex;align-items:center;gap:8px;font-family:"Montserrat",sans-serif;font-weight:800;color:#444;line-height:1.05;letter-spacing:.5px}
.brand .mark{width:22px;height:22px;background:#444;flex:none}
.spine{position:absolute;top:0;bottom:0;left:418px;width:14px;background:linear-gradient(90deg,rgba(0,0,0,0),rgba(0,0,0,.16),rgba(0,0,0,0))}
.small{font-size:7.5px;line-height:1.45}
h2,h3{font-family:"Montserrat",sans-serif}

/* cover */
.cover{left:374px;top:95px;width:448px;height:582px}
.cover .head{left:176px;top:0;width:272px;height:441px;background:var(--orange)}
.cover .contact{left:188px;top:28px;width:252px;display:flex;justify-content:space-between;color:#fff;font-size:6px;font-weight:700;align-items:center;line-height:1.3}
.cover .contact span{display:flex;align-items:center;gap:4px;white-space:nowrap}
.cover .date{left:273px;top:257px;width:149px;height:55px;background:var(--purple);color:#fff;font-family:"Oswald",sans-serif;font-size:30px;display:flex;align-items:center;justify-content:center}
.cover .title{left:67px;top:315px;width:306px;height:106px;border:2px solid #bbb;border-top:none;text-align:center;padding-top:14px}
.cover .title .l1{font-family:"Montserrat",sans-serif;color:var(--green);font-size:17px}
.cover .title .l2{font-family:"Montserrat",sans-serif;color:var(--green);font-size:18px;font-weight:700;letter-spacing:3px;margin-top:4px}
.cover .title .l3{font-family:"Montserrat",sans-serif;font-size:9.5px;letter-spacing:4.5px;margin-top:10px;font-weight:600}
.cover .foot{left:176px;top:540px;width:272px;height:42px;background:var(--orange)}

/* contents spread */
.spread{left:192px;width:850px;height:565px}
.contents{left:602px;top:334px;width:248px;height:213px;background:rgba(240,243,236,.88)}
.contents .bar{right:0;top:0;width:17px;height:100%;background:var(--amber)}
.contents h2{position:absolute;left:20px;top:16px;font-size:14px;color:var(--purple);font-weight:800}
.contents .rule{left:20px;top:38px;width:40px;height:2px;background:var(--orange)}
.toc{position:absolute;left:22px;top:75px;width:196px;list-style:none;font-size:7px}
.toc li{display:flex;justify-content:space-between;align-items:flex-end;border-bottom:1px solid #999;padding:6px 0 3px;text-transform:uppercase}
.toc li b{font-weight:700}

/* barricade spread */
.purple-page{left:0;top:0;width:425px;height:565px;background:var(--purple)}
.barricade h2{left:36px;top:43px;color:#fff;font-size:15.5px;font-weight:800;line-height:1.2}
.barricade .lead{left:36px;top:91px;width:360px;color:#fff;font-size:12.5px;line-height:1.3}
.barricade .body{left:36px;top:150px;width:370px;color:#e8e6f4}
.framed{border:3px solid #fff}
.specs{left:440px;top:259px;width:330px;height:306px;background:#fff;padding:12px 10px 0 42px;display:flex;flex-direction:column;gap:8px}
.spec{position:relative;font-size:6.4px;line-height:1.4}
.icon{position:absolute;left:-26px;top:0;width:13px;height:13px;border-radius:50%}
.reserve{margin-left:-24px;width:289px;border:2px solid var(--teal);text-align:center;font-size:6.4px;line-height:1.4;padding:8px 6px;margin-top:2px}

/* details spread */
.details h2{left:36px;top:51px;font-size:15px;line-height:1.1}
.sub{color:var(--orange);font-weight:700;font-size:7.5px}
.tbl{width:100%;border-collapse:collapse;font-size:6px;text-align:center}
.tbl th{font-weight:700;padding:2px}
.tbl td{padding:2px}
.tbl .alt td{background:var(--orange);color:#fff}
.tbl .first{font-style:italic;text-align:left}
</style>
</head>
<body>

<!-- Cover -->
<section class="page cover" aria-label="Cover">
  <div class="abs head"></div>
  <div class="abs brand" style="left:18px;top:22px;font-size:14px"><span class="mark"></span><span>HARBOR VALLEY<br>PRIDE</span></div>
  <div class="abs contact">
    <span><svg width="9" height="9" viewBox="0 0 10 10"><circle cx="5" cy="5" r="4.3" fill="none" stroke="#fff"/><rect x="2.8" y="3.5" width="4.4" height="3" fill="none" stroke="#fff" stroke-width=".8"/></svg>ads@harborvalleypride.org</span>
    <span><svg width="9" height="9" viewBox="0 0 10 10"><circle cx="5" cy="5" r="4.3" fill="none" stroke="#fff"/><rect x="3.5" y="2.5" width="3" height="5" rx=".6" fill="none" stroke="#fff" stroke-width=".8"/></svg>555-014-2290</span>
    <span><svg width="9" height="11" viewBox="0 0 10 12"><path d="M5 1a3.5 3.5 0 0 1 3.5 3.5C8.5 7 5 11 5 11S1.5 7 1.5 4.5A3.5 3.5 0 0 1 5 1z" fill="none" stroke="#fff"/><circle cx="5" cy="4.5" r="1.2" fill="#fff"/></svg><span style="display:block">P.O. Box 4417,<br>Harbor City, HV 10482</span></span>
  </div>
  <div class="photo" role="img" aria-label="Aerial photo of the festival grounds along the river with city skyline" style="left:0;top:81px;width:422px;height:231px"></div>
  <div class="abs date">JUNE 2019</div>
  <div class="abs title">
    <div class="l1">HARBOR VALLEY JOYFAIR</div>
    <div class="l2">AND NIGHT PARADE</div>
    <div class="l3">SPONSORSHIP PACKAGES</div>
  </div>
  <div class="photo" role="img" aria-label="Festival tents under rainbow canopies" style="left:0;top:441px;width:90px;height:99px;background:linear-gradient(160deg,#e9a0b8,#8fb7d9)"></div>
  <div class="photo" role="img" aria-label="Waving rainbow flag" style="left:92px;top:441px;width:110px;height:99px;background:linear-gradient(120deg,#e53935,#fb8c00,#fdd835,#43a047,#1e88e5,#8e24aa)"></div>
  <div class="photo" role="img" aria-label="Crowd with rainbow balloons and parade sign" style="left:204px;top:441px;width:90px;height:99px;background:linear-gradient(180deg,#d8c66a,#6a5a7a)"></div>
  <div class="photo" role="img" aria-label="Parade participants with sashes" style="left:296px;top:441px;width:152px;height:99px;background:linear-gradient(180deg,#a9bcc9,#b57f6a)"></div>
  <div class="abs foot"></div>
</section>

<!-- Contents spread -->
<section class="page spread" style="top:881px" aria-label="Contents spread">
  <div class="photo" role="img" aria-label="Panoramic view of the festival beside the river and downtown skyline" style="inset:0;width:850px;height:565px"></div>
  <div class="spine"></div>
  <div class="abs brand" style="left:30px;top:43px;width:194px;height:67px;background:#f4f4f4;padding-left:14px;font-size:16px"><span class="mark"></span><span>HARBOR VALLEY<br>PRIDE</span></div>
  <div class="abs contents">
    <div class="abs bar"></div>
    <h2>CONTENT</h2>
    <div class="abs rule"></div>
    <ul class="toc">
      <li><span>Barricade advertising opportunities</span><b>2</b></li>
      <li><span>Advertising details and deadlines</span><b>6</b></li>
      <li><span>Sponsorship details &amp; deadlines</span><b>8</b></li>
      <li><span>JoyFair pricing dates</span><b>9</b></li>
      <li><span>2019 sponsorship &amp; marketing<br>opportunities</span><b>11</b></li>
    </ul>
  </div>
</section>

<!-- Barricade spread -->
<section class="page spread barricade" style="top:1658px" aria-label="Barricade advertising spread">
  <div class="abs purple-page"></div>
  <div class="abs" style="left:425px;top:0;width:58px;height:237px;background:var(--purple-dark)"></div>
  <h2 class="abs">JoyFair &amp; Night Parade<br>Barricade Advertising Opportunities</h2>
  <p class="abs lead">Reach more than 75,000 people and advertise your business or organization at the HV JoyFair and New England’s only Illuminated Night Parade.</p>
  <p class="abs body small">Harbor Valley Pride is offering the opportunity to advertise on our barricades that will line the streets of downtown Harbor City for the parade and the HV JoyFair on Riverside Street. Be part of one of the largest events in the City of Harbor City.</p>
  <div class="photo framed" role="img" aria-label="Parade crowd behind a sponsor barricade banner" style="left:39px;top:211px;width:176px;height:112px;background:linear-gradient(180deg,#6d5360,#b59070)"></div>
  <div class="photo framed" role="img" aria-label="Sample sponsor banner mounted on a barricade" style="left:237px;top:211px;width:160px;height:112px;background:linear-gradient(180deg,#c7d6e4,#7d8fb7)"></div>
  <div class="photo" role="img" aria-label="Downtown bridge lined with rainbow banners" style="left:0;top:334px;width:425px;height:231px;background:linear-gradient(180deg,#5b8fcf 0%,#9cc1e3 45%,#9a8d84 80%,#62707f 100%)"></div>
  <div class="photo" role="img" aria-label="Visitors on a fair ride overlooking the festival" style="left:483px;top:0;width:367px;height:237px;background:linear-gradient(180deg,#6fa3d6,#9fc4e0 50%,#86a169)"></div>
  <div class="spine"></div>
  <div class="abs" style="left:770px;top:259px;width:80px;height:306px;background:var(--orange)"></div>
  <div class="abs specs">
    <div class="spec"><span class="icon" style="background:var(--orange)"></span><b>Advertising Costs:</b> $250 per section or $500 for three. This includes the cost of printing and production of the vinyl graphics. See below for submission of print ready artwork and space reservation.</div>
    <div class="spec"><span class="icon" style="background:var(--green)"></span><b>Design Services:</b> If you need additional design services, please contact us for an estimate.</div>
    <div class="spec"><span class="icon" style="background:var(--teal)"></span><b>Artwork Specs:</b> Banner size is 2.5’ x 6’ (71.80” x 30.20” with bleed)<br><b>Please submit art as a certified .PDF.</b> PDFs must meet PDF/X-1a standards with 300 dpi images, CMYK colors and embedded fonts. Export or “Save As” using the PDF/X-1a settings from Layoutly Pages (preferred), PixelForge, or VectorCraft. For quality-control purposes, advertisers who submit PDF files may be required to supply native files if the PDF is problematic.</div>
    <div class="spec"><span class="icon" style="background:var(--purple)"></span><b>Email final files to ads@harborvalleypride.org prior to June 1.</b> Deadlines &amp; Reservations:<br>Ad reservation deadline: May 24 Final artwork deadline: June 1</div>
    <div class="spec">Payment is due with ad reservation.</div>
    <div class="reserve">Please go to <b>www.HarborValleyPride.org/advertising</b> to reserve your spot or<br><b>email ads@harborvalleypride.org.</b><br><br><b>Questions? Contact us:</b><br>ads@harborvalleypride.org<br>555-014-2290<br>PO Box 4417, Harbor City, HV 10482</div>
  </div>
</section>

<!-- Details spread -->
<section class="page spread details" style="top:2442px" aria-label="Advertising details spread">
  <h2 class="abs"><span style="color:var(--orange);font-weight:400">ADVERTISING DETAILS</span><br><span style="color:var(--purple);font-weight:800">AND DEADLINES</span></h2>
  <div class="abs" style="left:36px;top:88px;width:26px;height:2px;background:var(--green)"></div>
  <div class="abs" style="left:36px;top:100px;width:230px">
    <p class="sub" style="font-size:7.5px">All artwork(s) should be sent to ads@harborvalleypride.org</p>
    <p class="sub" style="margin-top:14px">Payments for Advertising</p>
    <p class="small">Payments by check should be made out to <b>Harbor Valley Pride, Inc.</b> and send to <b>PO Box 4417 Harbor City, HV 10482.</b> <b>Please Note:</b> Advertisers must be paid in full no later than <b>May 1, 2019</b> for guaranteed inclusion in applicable advertising.</p>
    <p class="sub" style="margin-top:10px">Logo Requirements</p>
    <p class="small"><b>SUBMISSION DEADLINE: MAY 1, 2019</b></p>
    <p class="small">• PDF is the preferred format, with fonts embedded and graphics in grayscale or CMYK color mode.<br><i><b>Note:</b> If you cannot submit your logo as a PDF, you may also send it as a CMYK TIFF or JPEG image at 300dpi.</i></p>
    <p class="small" style="margin-top:8px">• Please provide the following versions of your logo:<br>&nbsp;&nbsp;o Full-color (CMYK)<br>&nbsp;&nbsp;o B&amp;W<br>&nbsp;&nbsp;o Reverse W&amp;B</p>
  </div>
  <div class="photo" role="img" aria-label="Festival-goers at a vendor booth" style="left:276px;top:28px;width:149px;height:197px;background:linear-gradient(180deg,#a9c6e0,#c77f8f)"></div>
  <div class="photo" role="img" aria-label="Group of friends celebrating with rainbow flags" style="left:276px;top:243px;width:149px;height:127px;background:linear-gradient(180deg,#9fc3e0,#e3a55a,#7f5f8f)"></div>
  <div class="abs" style="left:0;top:383px;width:425px;height:186px;background:var(--purple);color:#fff;padding:20px 36px">
    <p class="sub">JoyGuide Artwork</p>
    <p class="small"><b>SUBMISSION DEADLINE: MAY 1, 2019</b></p>
    <p class="small" style="margin-top:8px">• PDF is the preferred format, with fonts embedded and graphics in grayscale or CMYK color mode.<br><i>Note: If you cannot submit your ad as a PDF, you may also send it as a CMYK TIFF or JPEG image at 300dpi.</i></p>
    <table class="tbl" style="margin-top:6px;color:#fff">
      <tr><th></th><th>FULL PAGE</th><th>HALF PAGE</th><th>QUARTER PAGE</th></tr>
      <tr class="alt"><td class="first">Trim</td><td>5”w x 8”h</td><td>5”w x 3.875”h</td><td>2.375”w x 3.875”h</td></tr>
      <tr><td class="first">Bleed</td><td>5.25”w x 8.25”h</td><td>5.25”w x 4”h</td><td>2.5”w x 4”h</td></tr>
      <tr class="alt"><td class="first">Cost per ad</td><td>$450</td><td>$300</td><td>$95</td></tr>
    </table>
  </div>
  <div class="spine"></div>
  <div class="photo" role="img" aria-label="Festival visitor holding a printed portrait sign by the river" style="left:640px;top:6px;width:210px;height:206px;background:linear-gradient(180deg,#c7d5df,#93a78b)"></div>
  <div class="abs small" style="left:425px;top:43px;width:237px;height:133px;background:var(--purple);color:#fff;padding:12px 14px;font-size:6.6px;line-height:1.4">
    <b>TRIM AND BLEED:</b> The “trim” is the size of your ad as it will appear in the magazine. The “bleed” includes a .125” margin on all sides required to place and print your ad. The bleed is not visible once the magazine is printed – all live text and images in your ad must be within the trim dimensions, while background images or colors must extend to the bleed dimensions. All ads must have a .125” bleed on all four sides. We cannot print your ad without it. We also recommend to keep live text .25” from trim dimensions (a “safety” margin). Crop marks, targets, etc. are not required.
  </div>
  <div class="abs" style="left:455px;top:214px;width:370px">
    <p class="sub">Banner Advertising</p>
    <p class="small"><b>SUBMISSION DEADLINE: MAY 1, 2019</b></p>
    <p class="small">Harbor Valley Pride is offering the opportunity to advertise throughout the festival – banners will be displayed in a variety of locations to include the all of the festival grounds, and throughout the downtown area – lining the first and only Illuminated Pride Parade in New England. Be part of one of the largest events in the City of Harbor City.</p>
    <p class="small" style="margin-top:6px">• PDF is the preferred format, with fonts embedded and graphics in grayscale or <b>CMYK</b> color mode.<br><i>Note: If you cannot submit your ad as a PDF, you may also send it as a CMYK TIFF or JPEG image at 300dpi.</i></p>
    <table class="tbl" style="margin-top:8px;width:350px;margin-left:10px">
      <tr><th></th><th>STANDARD BANNER</th><th>FENCE BANNER</th></tr>
      <tr><td class="first" style="background:#cfe9e0">Finished size</td><td style="background:#cfe9e0">60”w x 30”h</td><td style="background:#cfe9e0">72”w x 54”h</td></tr>
      <tr><td class="first" style="border-bottom:1px solid #999">Cost per ad</td><td style="border-bottom:1px solid #999">$250<br>x3 $500</td><td style="border-bottom:1px solid #999">$500</td></tr>
    </table>
  </div>
  <div class="photo" role="img" aria-label="Rainbow festival tent with welcome banner by the river" style="left:425px;top:389px;width:286px;height:180px;background:linear-gradient(180deg,#a8c4dc,#d49a7a 60%,#8c8c8c)"></div>
  <div class="abs small" style="left:711px;top:389px;width:139px;height:180px;background:var(--teal);color:#fff;padding:16px 12px;font-size:6.8px">
    <b>Other advertising opportunities include:</b><br>• Entrance point banners<br>• Main-stage banners<br>• Main-stage LED board<br>&nbsp;&nbsp;- static ads<br>&nbsp;&nbsp;- video ads<br>• Spirits garden banners
  </div>
</section>

</body>
</html>
```